Melvin Otrasko Consulting Corporation
Independent Insurance and Reinsurance Consultants
Melvin Otrasko Consulting Corporation - Consulting
Creative Brief
Professional
Melvin Otrasko, MSc
Risk and Coverage Advisor
3816C Verlune Court Carlsbad, CA 92011
motrasko@motraskoadvise.com
www.motraskoadvise.com

```html
<!DOCTYPE html>
<html lang="en">
<head>
<meta charset="utf-8">
<title>Melvin Otrasko Consulting Corporation – Stationery</title>
<link rel="stylesheet" href="https://fonts.googleapis.com/css2?family=Tinos:wght@400&family=Open+Sans:wght@400;600&display=swap">
<style>
  :root {
    --canvas: #ededed;
    --paper: #ffffff;
    --blue-deep: #0b3a9a;
    --blue-mid: #1a62c8;
    --blue-bright: #27a0ea;
    --ink-blue: #1646a8;
    --ink-grey: #5d6570;
    --line-soft: #d8dde4;
    --window: #e9ebee;
    --emblem: #eef1f4;
  }
  * { box-sizing: border-box; margin: 0; padding: 0; }
  html, body { width: 1200px; height: 821px; overflow: hidden; }
  body { background: var(--canvas); position: relative; font-family: "Tinos", serif; }

  .sheet { position: absolute; background: var(--paper); box-shadow: 0 1px 4px rgba(0,0,0,.18); overflow: hidden; }

  .company { position: absolute; font-family: "Tinos", serif; font-weight: 400; color: var(--ink-blue); white-space: nowrap; line-height: 1; }

  .band-v { position: absolute; background: linear-gradient(180deg, var(--blue-deep) 0%, var(--blue-bright) 35%, var(--blue-mid) 60%, var(--blue-deep) 100%); }
  .band-v::after { content: ""; position: absolute; top: 0; right: 3px; width: 1px; height: 100%; background: rgba(255,255,255,.7); }

  .emblem { position: absolute; border-radius: 50%; background: radial-gradient(ellipse at 50% 50%, var(--emblem) 0%, rgba(238,241,244,.6) 50%, rgba(255,255,255,0) 72%); }

  /* Letterhead */
  .letterhead { left: 38px; top: 43px; width: 521px; height: 737px; }
  .letterhead .band-v { left: 0; top: 0; width: 26px; height: 100%; }
  .letterhead .company { left: 40px; top: 22px; font-size: 16px; }
  .letterhead .emblem { left: 120px; top: 250px; width: 300px; height: 320px; }

  /* Business card front */
  .card { border-radius: 8px; }
  .card-front { left: 763px; top: 77px; width: 300px; height: 158px; }
  .card-front .band-v { left: 0; top: 0; width: 14px; height: 100%; }
  .card-front .company { left: 24px; top: 20px; font-size: 12px; }
  .card-front .rule { position: absolute; left: 24px; top: 42px; width: 120px; height: 1px; background: var(--line-soft); }
  .card-front .emblem { left: 195px; top: 50px; width: 95px; height: 95px; }
  .contact { position: absolute; left: 24px; top: 58px; font-family: "Open Sans", sans-serif; font-size: 6.3px; color: var(--ink-grey); line-height: 1.35; }
  .contact .addr { margin-bottom: 7px; }
  .contact li { list-style: none; display: flex; align-items: center; gap: 4px; margin-bottom: 3px; }
  .contact svg { width: 7px; height: 7px; flex: none; }
  .holder { position: absolute; left: 168px; top: 98px; font-family: "Open Sans", sans-serif; color: var(--ink-blue); }
  .holder .person { font-size: 8.4px; font-weight: 600; display: block; }
  .holder .role { font-size: 6px; color: var(--ink-grey); display: block; margin-top: 2px; }

  /* Card backs */
  .card-white { left: 710px; top: 271px; width: 164px; height: 161px; }
  .card-blue { left: 888px; top: 271px; width: 175px; height: 161px; background: radial-gradient(ellipse at 45% 45%, var(--blue-bright) 0%, var(--blue-mid) 45%, var(--blue-deep) 100%); }
  .card-white .company, .card-blue .company { left: 0; width: 100%; top: 72px; text-align: center; font-size: 7.5px; }
  .card-blue .company { color: #ffffff; }
  .card-white .emblem { left: 52px; top: 40px; width: 60px; height: 75px; }
  .site { position: absolute; left: 0; width: 100%; bottom: 12px; text-align: center; font-family: "Open Sans", sans-serif; font-size: 5.6px; color: var(--ink-grey); }
  .card-blue .site { color: #dbe9fb; }

  /* Envelope */
  .envelope { left: 619px; top: 463px; width: 547px; height: 329px; }
  .envelope .flap { position: absolute; left: 0; top: 0; width: 100%; height: 78px; background: linear-gradient(180deg, var(--blue-deep) 0%, var(--blue-mid) 45%, var(--blue-bright) 75%, #e6f3fd 100%); }
  .envelope .flap .company { right: 140px; top: 20px; font-size: 15px; color: #ffffff; transform: rotate(180deg); }
  .envelope .band-v { left: 0; top: 78px; width: 18px; height: 251px; background: linear-gradient(180deg, var(--blue-bright), var(--blue-mid) 40%, var(--blue-deep)); }
  .envelope .body-company { left: 32px; top: 112px; font-size: 16px; }
  .envelope .window { position: absolute; left: 32px; top: 150px; width: 158px; height: 62px; border-radius: 8px; background: var(--window); border: 1px solid #dfe2e6; }
  .envelope .emblem { left: 380px; top: 185px; width: 140px; height: 130px; }
</style>
</head>
<body>

  <section class="sheet letterhead" aria-label="Letterhead">
    <div class="band-v"></div>
    <p class="company">Melvin Otrasko Consulting Corporation</p>
    <div class="emblem" role="img" aria-label="Faint scales of justice emblem"></div>
  </section>

  <section class="sheet card card-front" aria-label="Business card front">
    <div class="band-v"></div>
    <p class="company">Melvin Otrasko Consulting Corporation</p>
    <div class="rule"></div>
    <div class="emblem" role="img" aria-label="Faint scales of justice emblem"></div>
    <div class="contact">
      <p class="addr">3816C Verlune Court<br>Carlsbad, CA 92011</p>
      <ul>
        <li><svg viewBox="0 0 10 10"><path d="M2 1h2l1 2.5-1.3.8a6 6 0 0 0 2 2l.8-1.3L9 6v2a1 1 0 0 1-1 1A8 8 0 0 1 1 2a1 1 0 0 1 1-1z" fill="#1a62c8"/></svg>Office 760.555.0142</li>
        <li><svg viewBox="0 0 10 10"><rect x="2.5" y="0.5" width="5" height="9" rx="1" fill="#1a62c8"/></svg>Mobile 760.555.0187</li>
        <li><svg viewBox="0 0 10 10"><rect x="0.5" y="2" width="9" height="6" fill="#1a62c8"/><path d="M.5 2l4.5 3.5L9.5 2" stroke="#fff" fill="none" stroke-width=".8"/></svg>motrasko@motraskoadvise.com</li>
        <li><svg viewBox="0 0 10 10"><circle cx="5" cy="5" r="4.3" fill="none" stroke="#1a62c8" stroke-width="1.2"/><path d="M.7 5h8.6M5 .7c-2 2.5-2 6 0 8.6M5 .7c2 2.5 2 6 0 8.6" stroke="#1a62c8" fill="none" stroke-width=".7"/></svg>www.motraskoadvise.com</li>
      </ul>
    </div>
    <div class="holder">
      <span class="person">Melvin Otrasko, MSc</span>
      <span class="role">Risk and Coverage Advisor</span>
    </div>
  </section>

  <section class="sheet card card-white" aria-label="Business card back, white">
    <div class="emblem" role="img" aria-label="Faint scales of justice emblem"></div>
    <p class="company">Melvin Otrasko Consulting Corporation</p>
    <p class="site">www.motraskoadvise.com</p>
  </section>

  <section class="sheet card card-blue" aria-label="Business card back, blue">
    <p class="company">Melvin Otrasko Consulting Corporation</p>
    <p class="site">www.motraskoadvise.com</p>
  </section>

  <section class="sheet envelope" aria-label="Envelope">
    <div class="flap">
      <p class="company">Melvin Otrasko Consulting Corporation</p>
    </div>
    <div class="band-v"></div>
    <p class="company body-company">Melvin Otrasko Consulting Corporation</p>
    <div class="window"></div>
    <div class="emblem" role="img" aria-label="Faint scales of justice emblem"></div>
  </section>

</body>
</html>
```